Marlow Hire Business Card for recruitment company

We are looking for a Business Card Design that incorporates our personal details and our busines name and logo. We are a specialized search consultancy that recruit Property and Construction professionals.
We would like a business card that stands out and is appealing to the Construction and Property industry as well.

Target Market(s)

people in the construction and property industry

Contact Information for Business Card

Business Name and logo

Font styles to use
Serif

Colors
0094D4
00A9DD
6FCCEA
C7EBF8
E9F6FB

Requirements
Must have
• Business name and logo as well as contact details
Should not have
• No photos of us please

```html
<!DOCTYPE html>
<html lang="en">
<head>
<meta charset="utf-8">
<title>Marlow Hire – Business Card</title>
<link href="https://fonts.googleapis.com/css2?family=Josefin+Sans:wght@300&family=Playfair+Display:wght@400&family=Roboto:wght@400&display=swap" rel="stylesheet">
<style>
  :root {
    --backdrop: #6e9baa;
    --navy: #043d52;
    --slate: #7f9ea9;
    --paper: #ffffff;
    --skyline-light: #a9bcc3;
    --skyline-mid: #7d9aa4;
    --skyline-dark: #5e808c;
  }
  * { margin: 0; padding: 0; box-sizing: border-box; }
  html, body { width: 1200px; height: 800px; overflow: hidden; }
  body {
    background: var(--backdrop);
    display: flex;
    align-items: center;
    justify-content: center;
    gap: 40px;
  }
  .card {
    position: relative;
    width: 540px;
    height: 350px;
    overflow: hidden;
  }
  .card--front { background: var(--navy); }
  .card--back { background: var(--paper); }

  .brand-name {
    position: absolute;
    font-family: "Josefin Sans", sans-serif;
    font-weight: 300;
    text-transform: uppercase;
    white-space: nowrap;
    line-height: 1;
  }
  .card--front .brand-name {
    left: 0; right: 0;
    top: 152px;
    text-align: center;
    font-size: 50px;
    letter-spacing: 2px;
    color: var(--paper);
  }
  .card--back .brand-name {
    left: 30px;
    top: 166px;
    font-size: 27px;
    letter-spacing: 1px;
    color: var(--navy);
  }

  .skyline {
    position: absolute;
    left: 10px;
    bottom: 10px;
    height: 100px;
  }
  .card--front .skyline {
    right: 10px;
    background: linear-gradient(to bottom, var(--skyline-dark), var(--skyline-light));
    opacity: 0.85;
  }
  .card--back .skyline {
    width: 360px;
    background: linear-gradient(to bottom, #eef2f3, var(--skyline-light) 45%, var(--skyline-mid));
  }

  .panel {
    position: absolute;
    inset: 0;
    width: 100%;
    height: 100%;
  }

  .holder {
    position: absolute;
    right: 36px;
    top: 88px;
    text-align: right;
    color: var(--paper);
  }
  .holder__name {
    font-family: "Playfair Display", serif;
    font-weight: 400;
    font-size: 36px;
    line-height: 1.1;
  }
  .holder__role {
    font-family: "Roboto", sans-serif;
    font-size: 11.5px;
    margin-top: 2px;
  }
  .divider {
    position: absolute;
    left: 337px;
    width: 167px;
    top: 158px;
    height: 2px;
    background: var(--paper);
  }
  .contact {
    position: absolute;
    font-family: "Roboto", sans-serif;
    font-size: 11px;
    color: var(--paper);
    line-height: 1.3;
    white-space: nowrap;
  }
  .contact--address { left: 337px; top: 176px; }
  .contact--phone { left: 344px; top: 247px; }
  .contact--email { left: 359px; top: 270px; }
  .contact--web { left: 378px; top: 293px; }
</style>
</head>
<body>

  <section class="card card--front" aria-label="Business card front">
    <div class="skyline" role="img" aria-label="City skyline silhouette in layered teal tones"></div>
    <p class="brand-name">Marlow Hire</p>
  </section>

  <section class="card card--back" aria-label="Business card back">
    <div class="skyline" role="img" aria-label="City skyline silhouette in pale grey-teal tones"></div>
    <svg class="panel" viewBox="0 0 540 350" preserveAspectRatio="none" aria-hidden="true">
      <polygon points="352,9 382,9 258,175 382,340 352,340 256,175" fill="var(--slate)"/>
      <polygon points="382,9 531,9 531,340 382,340 258,175" fill="var(--navy)"/>
    </svg>
    <p class="brand-name">Marlow Hire</p>

    <div class="holder">
      <h1 class="holder__name">Evan Hale</h1>
      <p class="holder__role">Senior Search Consultant</p>
    </div>
    <div class="divider"></div>
    <p class="contact contact--address">48 Kestrel Lane, Harbourton,<br>NW 20418</p>
    <p class="contact contact--phone">T : 555-014-2290</p>
    <p class="contact contact--email">E : hello@marlowhire.com</p>
    <p class="contact contact--web">W : www.marlowhire.com</p>
  </section>

</body>
</html>
```